Whimsical business cards and stationary for accessories and gifts company
Please use your design expertise!
Whimsical business cards and stationary for accessories and gifts company - Children
Creative Brief
Bright & Fun-filled
Marisa T Palvendo
Designer
Somerset, New Jersey
PipandLulaDesigns@brimletmail.com
www.PipAndLulaDesigns.craftvane.com www.friendloop.com/PipandLulaDesigns @PipAndLulaDesigns
Hair Accessories Party Favors Unique Gifts
Concepts
Business Cards for kids golf
Vanta Vanta
Kindly upload the Ai file of your logo.

```html
<!DOCTYPE html>
<html lang="en">
<head>
<meta charset="utf-8">
<title>Pip &amp; Lula Designs — Business Card</title>
<link rel="stylesheet" href="https://fonts.googleapis.com/css2?family=Josefin+Sans:wght@300;400;600&display=swap">
<style>
  :root{
    --plum:#a24f9b;
    --plum-light:#b96bb3;
    --plum-dark:#863d80;
    --lilac:#e3c6e0;
    --paper:#ffffff;
    --stage:#ece9ea;
    --ink-soft:#f6e9f5;
  }
  *{box-sizing:border-box;margin:0;padding:0}
  html,body{width:1200px;height:904px;overflow:hidden}
  body{background:var(--stage);font-family:"Josefin Sans",sans-serif;position:relative}
  .card{position:absolute;left:250px;width:700px;height:400px;border-radius:4px;overflow:hidden;box-shadow:0 6px 18px rgba(0,0,0,.15)}
  .card--back{top:32px;background:linear-gradient(160deg,var(--plum-light),var(--plum))}
  .card--front{top:472px;background:var(--paper)}

  .wordmark{display:flex;align-items:center;gap:10px;color:var(--paper);font-weight:600;letter-spacing:.02em}
  .wordmark__dot{border-radius:50%;flex:none}

  .card--back .wordmark{position:absolute;left:50%;top:130px;transform:translateX(-50%);font-size:40px}
  .card--back .wordmark__dot{width:30px;height:30px;background:var(--plum-dark)}
  .services{position:absolute;left:0;right:0;top:292px;text-align:center;color:var(--ink-soft);font-size:15px;font-weight:300;letter-spacing:.04em}
  .services span{margin:0 10px}

  .brand{position:absolute;left:48px;top:44px}
  .brand .wordmark{color:var(--plum);font-size:34px}
  .brand .wordmark__dot{width:22px;height:22px;background:var(--plum)}
  .brand__tag{margin:4px 0 0 32px;font-size:11px;color:var(--plum);font-weight:300;letter-spacing:.2em;text-transform:lowercase}

  .band{position:absolute;left:0;top:170px;width:560px;height:230px;background:var(--plum)}
  .emblem{position:absolute;right:-40px;top:60px;width:300px;height:300px;border-radius:50%;background:var(--paper);border:16px solid var(--plum);display:flex;align-items:center;justify-content:center}
  .emblem .wordmark{color:var(--plum);font-size:30px;margin-left:-40px}
  .emblem .wordmark__dot{width:20px;height:20px;background:var(--lilac)}

  .person{position:absolute;left:48px;top:190px;color:var(--paper)}
  .person__name{font-size:20px;font-weight:400;letter-spacing:.02em}
  .person__role{font-size:12px;font-weight:300;margin-top:3px}
  .contacts{list-style:none;margin-top:14px}
  .contacts li{display:flex;align-items:center;gap:10px;font-size:12.5px;font-weight:300;line-height:22px}
  .contacts svg{flex:none}
</style>
</head>
<body>
  <section class="card card--back">
    <div class="wordmark"><span class="wordmark__dot"></span>pip &amp; lula</div>
    <p class="services"><span>Hair Accessories</span>|<span>Party Favors</span>|<span>Unique Gifts</span></p>
  </section>

  <section class="card card--front">
    <div class="brand">
      <div class="wordmark"><span class="wordmark__dot"></span>pip &amp; lula</div>
      <p class="brand__tag">handmade gifts</p>
    </div>
    <div class="band"></div>
    <div class="emblem"><div class="wordmark"><span class="wordmark__dot"></span>pip &amp; lula</div></div>
    <div class="person">
      <h1 class="person__name">Marisa T Palvendo</h1>
      <p class="person__role">Designer</p>
      <ul class="contacts">
        <li><svg width="12" height="12" viewBox="0 0 12 12"><path d="M3 1l2 2-1 1.5a7 7 0 003.5 3.5L9 7l2 2-1.5 2C5 11 1 7 1 2.5z" fill="#fff"/></svg>(555) 014-2287</li>
        <li><svg width="12" height="12" viewBox="0 0 12 12"><rect x="1" y="2.5" width="10" height="7" fill="none" stroke="#fff"/><path d="M1 2.5l5 4 5-4" fill="none" stroke="#fff"/></svg>PipandLulaDesigns@brimletmail.com</li>
        <li><svg width="12" height="12" viewBox="0 0 12 12"><circle cx="6" cy="6" r="5" fill="none" stroke="#fff"/><path d="M1 6h10M6 1v10" stroke="#fff" stroke-width=".8"/></svg>www.PipAndLulaDesigns.craftvane.com</li>
        <li><svg width="12" height="12" viewBox="0 0 12 12"><circle cx="6" cy="6" r="5" fill="#fff"/></svg>www.friendloop.com/PipandLulaDesigns</li>
        <li><svg width="12" height="12" viewBox="0 0 12 12"><circle cx="6" cy="6" r="5" fill="#fff"/></svg>@PipAndLulaDesigns</li>
      </ul>
    </div>
  </section>
</body>
</html>
```